Business Card Design Project

I require a business card design that looks professional for a small building company. Holloway Builders is the name of the company and i don't want to use a house or building design for a logo. I require a logo design for the card incorporating the name Holloway Builders but designed smartly.

We are a Registered Building Practitioner so the small logo attached must also be used on the card.

We cover a large range of Building / Construction, Concrete, Steelwork. Not sure how to implement this.

Colors are flexible, maybe a dark grey background with white writting over it, but i am keen to see other options.

Thanks.

Target Market(s)

Anyone

Industry/Entity Type

Building

Requirements
Must have
• The logo attached must be incorporated - can be small
A logo for my company needs to be included - using Holloway Builders as the base with no picture of a house or buildings.

```html
<!DOCTYPE html>
<html lang="en">
<head>
<meta charset="utf-8">
<title>Holloway Builders – Business Card</title>
<link rel="stylesheet" href="https://fonts.googleapis.com/css2?family=Fira+Sans:wght@500;600&display=swap">
<style>
  :root {
    --stage: #2b2b2b;
    --green-deep: #0f2a0c;
    --green-dark: #2b4a22;
    --green-mid: #4e6b33;
    --green-bright: #8cc63f;
    --paper: #ffffff;
    --ink: #1a1a1a;
    --badge-grey: #d9d9d9;
    --badge-edge: #6b6b6b;
  }
  * { box-sizing: border-box; margin: 0; padding: 0; }
  html, body { width: 1200px; height: 900px; overflow: hidden; }
  body {
    background: var(--stage);
    font-family: "Fira Sans", Arial, sans-serif;
    position: relative;
  }
  .card {
    position: absolute;
    width: 540px;
    height: 310px;
    overflow: hidden;
    box-shadow: 0 10px 24px rgba(0,0,0,0.45);
  }

  /* Front */
  .card--front {
    left: 50px; top: 150px;
    background: radial-gradient(circle at 42% 34%, var(--green-mid) 0%, #1f3f17 35%, var(--green-deep) 80%);
  }
  .card--front .brand {
    position: absolute;
    left: 0; right: 40px; top: 82px;
    display: flex; flex-direction: column; align-items: center; gap: 14px;
  }
  .brand__square {
    width: 64px; height: 64px;
    background: var(--green-bright);
  }
  .brand__name {
    font-weight: 600;
    font-size: 24px;
    color: var(--green-bright);
    letter-spacing: 0.2px;
  }
  .card--front .accent-line {
    position: absolute;
    left: 0; right: 0; top: 262px;
    height: 2px;
    background: var(--green-bright);
  }

  /* Back */
  .card--back {
    left: 610px; top: 440px;
    background: var(--paper);
  }
  .name-band {
    position: absolute;
    left: 0; top: 118px;
    width: 300px; height: 80px;
    background: var(--green-dark);
    display: flex; align-items: center;
    padding-left: 62px;
  }
  .name-band__name {
    color: var(--paper);
    font-weight: 600;
    font-size: 18px;
  }
  .corner-block {
    position: absolute;
    left: 470px; top: 38px;
    width: 70px; height: 80px;
    background: var(--green-dark);
  }
  .card--back .brand {
    position: absolute;
    left: 316px; top: 42px;
    width: 150px;
    display: flex; flex-direction: column; align-items: center; gap: 10px;
  }
  .card--back .brand__square {
    width: 54px; height: 54px;
    background: var(--green-dark);
  }
  .card--back .brand__name { font-size: 19px; }
  .registration-badge {
    position: absolute;
    left: 360px; top: 204px;
    width: 54px; height: 54px;
    border-radius: 50%;
    background: var(--badge-grey);
    border: 2px solid var(--badge-edge);
  }
  .contact {
    position: absolute;
    left: 100px; top: 222px;
    font-weight: 600;
    font-size: 11px;
    line-height: 1.45;
    color: var(--ink);
  }
  .contact__address { margin-bottom: 10px; }
  .contact__row { display: flex; }
  .contact__label { width: 52px; }
</style>
</head>
<body>

  <section class="card card--front" aria-label="Business card front">
    <div class="brand">
      <span class="brand__square" aria-hidden="true"></span>
      <span class="brand__name">Holloway Builders</span>
    </div>
    <div class="accent-line"></div>
  </section>

  <section class="card card--back" aria-label="Business card back">
    <div class="corner-block"></div>
    <div class="brand">
      <span class="brand__square" aria-hidden="true"></span>
      <span class="brand__name">Holloway Builders</span>
    </div>
    <div class="name-band">
      <span class="name-band__name">Daniel Holloway</span>
    </div>
    <div class="registration-badge" role="img" aria-label="Registered building practitioner badge"></div>
    <div class="contact">
      <p class="contact__address">42 Ridge Road<br>Ballan VIC 3342</p>
      <p class="contact__row"><span class="contact__label">Phone:</span><span>0412 555 019</span></p>
      <p class="contact__row"><span class="contact__label">Email:</span><span>holloway@mailbox.com.au</span></p>
    </div>
  </section>

</body>
</html>
```